Sports Event - Web Design Project

We run an event called GRIT & GLORY which is "Ireland's Fiercest 10K Trial" - so running through water, covered in mud, through electric fences etc. Similar type event to GrimSlogger or Valkoran Dash internationally

Have 2,500 people signed up for next event in January so want to revamp our current website www.gritandglory.ie and bring it up to the next level.

We are looking for 3 pages to be deisgned: a template site page, a Home Page & an Events Page with interactive map. I have already made a "home made" design of what we want - so this design will give you a good idea of the style and colours we want...then its up to you to add your skill and personality to make the new website exciting, stylish and professional.
Updates

I have just posted a web page which gives a bit more detail about the 3 pages we are looking for, the style etc

we have our own web developers who will take your design and implement it into the back end of our customised website...so whoever gets the job, I will get them to speak with our developer about what is the best way to give the final artwork etc to us. 

Here is the webpage with our "Homemade" designs on it to give you an idea of all the things we are looking for

http://www.wildroamco.ie/News/New-Website-Screenshots-post-35.htm

Here is the GRIT & GLORY logo - sorry dont know how else up to upload it

For the Interactive Map (Event Page), go to the following link for actual course:

Target Market(s)

Male and female, sporty and non-sporty (lots of people do this event for charity). Aged 21-45. People looking for a fun challenge

Industry/Entity Type

Events

Requirements
Must have
• Require 3 pages:
1. Home Page (with video being central point)
2. Events Page with interactive map
3. Template Site Page

See this link for more info:

We also require each of these designs to be enabled in the following formats:
1. PC / Desktop
2. iPad / Tablet
3. Phone

Must use the orange, red and black of GRIT & GLORY logo, as well as some type of hellish fire/flames

```html
<!DOCTYPE html>
<html lang="en">
<head>
<meta charset="utf-8">
<title>GRIT &amp; GLORY – Ireland's Fiercest 10K Trial</title>
<link href="https://fonts.googleapis.com/css2?family=Carlito:wght@400;700&display=swap" rel="stylesheet">
<style>
:root{
  --fire:#f7801e;
  --fire-light:#fba23a;
  --fire-deep:#e4600f;
  --ember:#7a1408;
  --ember-dark:#5e0c05;
  --soil:#3d3716;
  --ground:#4e4a25;
  --olive-text:#4b3d10;
  --cream:#fbeedd;
  --white:#ffffff;
  --btn-orange:#f36c10;
}
*{box-sizing:border-box;margin:0;padding:0}
html,body{width:1200px;height:1000px;overflow:hidden}
body{
  font-family:"Carlito","Calibri",sans-serif;
  background:radial-gradient(ellipse at 45% 40%,var(--fire-light) 0%,var(--fire) 45%,var(--fire-deep) 100%);
  position:relative;color:var(--white);
}
.abs{position:absolute}
.topbar{left:0;top:0;width:1200px;height:22px;background:var(--soil);border-bottom:2px solid #8a6a1c}
.topbar .tagline{left:123px;top:4px;font-size:12px;font-weight:700}
.social{left:302px;top:2px;display:flex;gap:3px}
.social span{width:17px;height:17px;background:#d9d2b8;display:block}
.utility{right:123px;top:0;display:flex;height:22px}
.utility a{color:var(--white);text-decoration:none;font-size:14px;padding:3px 11px 0;border-left:2px solid #6d6440;height:22px}
.utility a:last-child{border-right:2px solid #6d6440}
.nav{top:93px;height:54px;border-top:3px solid #8a4a10;border-bottom:3px solid #8a4a10;display:flex;align-items:center;gap:29px;font-size:25px}
.nav a{color:var(--cream);text-decoration:none}
.nav a.current{color:var(--ember)}
.nav-left{left:120px;width:384px;padding-left:29px}
.nav-right{left:697px;width:383px;justify-content:flex-end;padding-right:15px}
.brandmark{left:525px;top:40px;width:153px;height:153px;background:var(--fire-deep);border:1px solid var(--ember);display:flex;align-items:center;justify-content:center;flex-direction:column;gap:8px}
.brandmark .sq{width:14px;height:14px;background:var(--white)}
.brandmark .name{font-size:22px;font-weight:700;color:var(--white);text-align:center;line-height:1.05}
.video{left:135px;top:206px;width:426px;height:322px;background:var(--soil);border-radius:4px;padding:5px}
.video .title{height:30px;background:#111;font-family:Arial,sans-serif;font-size:14px;padding:7px 11px 0;color:var(--white)}
.video .frame{height:252px;background:linear-gradient(160deg,#4f5c38 0%,#3b3a2c 45%,#5a5444 100%)}
.video .base{height:30px;background:#050505}
.headline{left:648px;top:227px;font-size:41.5px;font-weight:700;line-height:49px;color:var(--cream);white-space:nowrap}
.headline em{font-style:normal;color:var(--ember)}
.register{left:920px;top:284px;width:145px;height:81px;background:var(--ember);border:1px solid var(--white);font-size:27px;font-weight:700;text-align:center;line-height:34px;padding-top:6px;color:var(--cream)}
.subhead{left:648px;top:386px;font-size:27px;font-weight:700;color:var(--olive-text)}
.journey{left:648px;top:441px;width:193px;height:68px;background:var(--soil);border-radius:5px;font-size:19px;font-weight:700;text-align:center;line-height:17px;padding-top:16px;color:var(--cream)}
.signup{left:865px;top:441px;width:192px;height:68px;background:var(--soil);border-radius:5px;padding:4px 13px}
.signup .label{font-size:16px;font-weight:700;color:var(--cream)}
.signup .field{position:absolute;left:12px;top:27px;width:123px;height:31px;background:var(--cream);border-radius:4px;font-size:11px;color:#333;padding:9px 7px}
.signup .join{position:absolute;left:143px;top:27px;width:40px;height:30px;background:var(--btn-orange);border:1px solid var(--cream);border-radius:5px;font-size:13px;font-weight:700;color:var(--soil);text-align:center;padding-top:6px}
.intro-title{left:137px;top:541px;font-size:20px;font-weight:700;color:var(--olive-text)}
.intro{left:137px;top:577px;width:420px;font-size:14px;font-weight:700;line-height:16.6px;color:var(--cream)}
.intro a{color:var(--ember);text-decoration:none}
.dates{left:135px;top:684px;width:482px;height:106px;background:var(--soil);border:1px solid var(--cream);padding:7px 13px}
.dates .label{font-size:17px;font-weight:700;color:var(--cream)}
.dates .label span{color:var(--btn-orange)}
.dates .row{display:flex;gap:13px;margin-top:8px}
.dates .date{width:103px;height:61px;background:var(--btn-orange);font-size:16px;font-weight:700;color:var(--ember-dark);text-align:center;line-height:17px;padding-top:12px}
.dates .date:first-child{border:1px solid var(--cream)}
.dates .date:nth-child(4){margin-left:6px}
.section-title{font-size:20px;font-weight:700;color:var(--olive-text)}
.partners-title{left:644px;top:540px}
.carousel{left:630px;top:570px;width:456px;height:62px;display:flex;align-items:center;justify-content:space-between}
.carousel .badge{width:130px;height:40px;border-radius:5px;background:rgba(255,255,255,0.22)}
.charity-title{left:644px;top:659px}
.charity-text{left:648px;top:699px;width:222px;font-size:14px;font-weight:700;line-height:16.6px;color:var(--cream)}
.charity-text b{color:var(--soil)}
.charity-badge{left:896px;top:690px;width:174px;height:103px;background:var(--white);border:2px solid #2c4aa0;border-radius:9px}
.ground{left:0;top:805px;width:1200px;height:195px}
.footer-col{top:834px;display:flex;flex-direction:column;gap:4.3px;font-size:13.5px}
.footer-col a{color:var(--white);text-decoration:none}
.copyright{right:122px;top:957px;font-size:13.5px}
</style>
</head>
<body>
<header>
  <div class="abs topbar">
    <span class="abs tagline">Ireland's Fiercest 10K Trial</span>
    <div class="abs social"><span></span><span></span><span></span></div>
    <nav class="abs utility"><a href="#">GET INVOLVED</a><a href="#">FAQ'S</a><a href="#">CONTACT US</a></nav>
  </div>
  <nav class="abs nav nav-left"><a class="current" href="#">Home</a><a href="#">Events</a><a href="#">Hall Of Fame</a></nav>
  <div class="abs brandmark"><span class="sq"></span><span class="name">GRIT &amp;<br>GLORY</span></div>
  <nav class="abs nav nav-right"><a href="#">Photos</a><a href="#">Videos</a><a href="#">Who Are We?</a></nav>
</header>

<main>
  <div class="abs video">
    <div class="title">Ireland's Fiercest 10K Trial - GRIT &amp; GLORY...</div>
    <div class="frame" role="img" aria-label="Video still of muddy runners crawling through a forest trail"></div>
    <div class="base"></div>
  </div>

  <h1 class="abs headline">Are you <em>TOUGH</em> enough<br>to make it thru<br><em>GRIT</em> &amp; GLORY?</h1>
  <a class="abs register">REGISTER<br>TODAY</a>
  <h2 class="abs subhead">Ireland's Fiercest 10K Trial</h2>
  <a class="abs journey">View Your Jouney<br>To Hell! Click Here</a>
  <div class="abs signup">
    <div class="label">Devils Unite!</div>
    <div class="field">Enter Your Email</div>
    <div class="join">Join</div>
  </div>

  <h2 class="abs intro-title">Ireland's Fiercest 10K Trial</h2>
  <p class="abs intro">Designed, built and customised by a former member of Elite Summit Scout Corps, the GRIT &amp; GLORY Challenge has now been tested and approved by the best – and is unique in commanding endurance beyond belief! With military precision, it will torment you physically and mentally. <a href="#">FIND OUT MORE!</a></p>

  <div class="abs dates">
    <div class="label">New Date's Added! - <span>Select Your Event</span></div>
    <div class="row">
      <div class="date">3rd Feb<br>2013</div>
      <div class="date">16th June<br>2013</div>
      <div class="date">23rd Oct<br>2013</div>
      <div class="date">18th June<br>2014</div>
    </div>
  </div>

  <h2 class="abs section-title partners-title">Our Partners</h2>
  <div class="abs carousel">
    <svg width="18" height="18" viewBox="0 0 18 18"><circle cx="9" cy="9" r="8" fill="#f7a040" stroke="#3d3716" stroke-width="1.5"/><path d="M11 4.5 6 9l5 4.5z" fill="#3d3716"/></svg>
    <div class="badge" aria-label="Partner badge"></div>
    <div class="badge" aria-label="Partner badge"></div>
    <div class="badge" aria-label="Partner badge"></div>
    <svg width="18" height="18" viewBox="0 0 18 18"><circle cx="9" cy="9" r="8" fill="#f7a040" stroke="#3d3716" stroke-width="1.5"/><path d="M7 4.5 12 9l-5 4.5z" fill="#3d3716"/></svg>
  </div>

  <h2 class="abs section-title charity-title">Raising Money For Charity</h2>
  <p class="abs charity-text">If you would like to raise money for your favourite charity, simply visit <b>www.givecircle.ie</b> where you can choose the charity you would like to support.</p>
  <div class="abs charity-badge" aria-label="Charity partner badge"></div>
</main>

<footer>
  <svg class="abs ground" viewBox="0 0 1200 195" preserveAspectRatio="none" aria-hidden="true">
    <path d="M0 10 Q20 2 40 8 Q60 3 80 9 Q100 2 120 8 Q140 3 160 9 Q180 2 200 8 Q220 3 240 9 Q260 2 280 8 Q300 3 320 9 Q340 2 360 8 Q380 3 400 9 Q420 2 440 8 Q460 3 480 9 Q500 2 520 8 Q540 3 560 9 Q580 2 600 8 Q620 3 640 9 Q660 2 680 8 Q700 3 720 9 Q740 2 760 8 Q780 3 800 9 Q820 2 840 8 Q860 3 880 9 Q900 2 920 8 Q940 3 960 9 Q980 2 1000 8 Q1020 3 1040 9 Q1060 2 1080 8 Q1100 3 1120 9 Q1140 2 1160 8 Q1180 3 1200 9 V195 H0Z" fill="#4e4a25"/>
    <path d="M0 185 Q150 174 300 180 Q450 186 600 178 Q750 172 900 181 Q1050 187 1200 177 V195 H0Z" fill="#7a1408"/>
  </svg>
  <nav class="abs footer-col" style="left:139px"><a href="#">Home</a><a href="#">Events</a><a href="#">Hall Of Fame</a><a href="#">Photos</a><a href="#">Videos</a><a href="#">Who are we?</a></nav>
  <nav class="abs footer-col" style="left:271px"><a href="#">Get Involved</a><a href="#">FAQ's</a><a href="#">Contact Us</a><a href="#">Your Charity</a><a href="#">Newsletter</a></nav>
  <nav class="abs footer-col" style="left:402px"><a href="#">Location</a><a href="#">Course</a><a href="#">Social Network</a></nav>
  <p class="abs copyright">© Copyright GRIT &amp; GLORY. 2012. All Rights Reserved</p>
</footer>
</body>
</html>
```